Business website cyber security

Full redesign of our current business website, mockup and powerpoint presentation have been provided.
Some animated elements (example: SVG with CSS) are welcome.
A detailed requirement list can also be found in the attached powerpoint
Also uploaded is the current page as a nicepage & html export. All 11 sites shall be reworked. "Branches", "Download", "Contact" and "Legal Information" are not needed .

A good example of a competitor is https://www.brantvolo.de/ this. Not in terms of colors, but in regard to website structure, animated elements and overall look.

Target Market(s)

Cyber security for the B2B market

Industry/Entity Type

IT, IT Security, banking

Coding

Coded - Design and coding required

Number of Pages Required

5+ page

Font styles to use
Other font styles liked:
• ReadexPro Regular, ReadexPro Light

Colors
0054AA
0677BA
7BADD7
CADEEF
E8F1F8

Requirements
Must have
• Modern and sleek design, corporate identity
Nice to have
• Animated elements (css svg)
Should not have
• too many colors (max 4), too fancy

```html
<!DOCTYPE html>
<html lang="de">
<head>
<meta charset="utf-8">
<title>Corvane – IT-Security · Compliance</title>
<link rel="stylesheet" href="https://fonts.googleapis.com/css2?family=Readex+Pro:wght@300;400;500;600&display=swap">
<style>
:root{
  --brand:#0054AA;
  --brand-2:#0677BA;
  --sky:#7BADD7;
  --pale:#CADEEF;
  --mist:#E8F1F8;
  --accent:#4d93e6;
  --navy:#0a2342;
  --navy-2:#0c2f59;
  --card:#0d3a6c;
  --footer:#0b3869;
  --footer-base:#071c37;
  --white:#ffffff;
}
*{box-sizing:border-box;margin:0;padding:0}
html,body{width:1200px;height:3628px;overflow:hidden}
body{font-family:"Readex Pro",sans-serif;color:var(--white);
  background:linear-gradient(180deg,var(--navy) 0,var(--navy) 620px,#0b2a52 900px,#0b2c56 1600px,#0c3766 1900px,#0b2d57 2200px,#0a2747 3393px);
  position:relative}
.abs{position:absolute}

/* header */
.site-header{left:0;top:0;width:1200px;height:88px;background:#0c2c54}
.nav-link{top:33px;font-size:14px;color:var(--white)}
.nav-link.active{text-decoration:underline;text-underline-offset:4px}
.brand-badge{left:545px;top:6px;width:110px;height:110px;border-radius:50%;background:var(--white);border:3px solid var(--brand);display:flex;flex-direction:column;align-items:center;justify-content:center;color:var(--brand);z-index:3}
.brand-badge b{font-weight:600;font-size:22px;letter-spacing:.5px}
.brand-badge small{font-size:7px;color:var(--navy)}
.flag{left:1079px;top:34px;width:32px;height:21px}

/* hero */
.hero-title{left:88px;top:205px;width:500px;font-size:38px;line-height:43px;font-weight:600;color:var(--accent)}
.hero-text{left:88px;top:362px;width:450px;font-size:14px;line-height:21px;font-weight:300}
.hero-visual{left:584px;top:88px;width:616px;height:492px;clip-path:polygon(50px 0,616px 0,616px 492px,0 492px);
  background:radial-gradient(circle at 45% 45%,#39b8ff 0,#1a5ed8 35%,#15307f 65%,#0d1f55 100%)}

/* services */
.service-card{top:660px;width:326px;height:179px;background:var(--card);border-radius:3px;padding:18px 14px 0 110px}
.service-card svg{position:absolute;left:26px;top:60px;width:62px;height:62px}
.service-card h3{font-size:17px;line-height:22px;font-weight:500;color:var(--accent);margin-bottom:6px}
.service-card p{font-size:12.5px;line-height:18px;font-weight:300}

/* vision */
.section-title{left:0;width:1200px;text-align:center;font-size:34px;font-weight:500}
.section-sub{left:0;width:1200px;text-align:center;font-size:12.5px;font-weight:300}
.tab{left:148px;width:152px;height:53px;background:var(--brand);display:flex;align-items:center;justify-content:center;font-size:16px;border-radius:2px}
.tab.current{background:#0c3462}
.vision-panel{left:315px;top:984px;width:728px;height:318px;background:#b6d4f6;color:var(--navy);padding:34px 32px;font-size:14px;line-height:19px}
.vision-panel h4{font-size:20px;font-weight:500;color:#123b73;margin-bottom:12px}
.vision-panel h5{font-size:14px;font-weight:500;color:#123b73;margin:16px 0 8px}
.vision-panel p{margin-bottom:10px}

/* sectors */
.sector-tile{width:325px;height:196px;border-radius:3px;display:flex;align-items:flex-end;justify-content:center;padding-bottom:14px;font-size:16px;font-weight:500}
.sector-ops{background:linear-gradient(180deg,#102b4c,#02080f);display:block;padding:30px 0 0 70px}
.sector-ops h3{font-size:24px;font-weight:600;margin-bottom:10px}
.sector-ops li{list-style:none;font-size:14px;line-height:25px}
.sector-ops li::before{content:"▸ ";font-size:10px}
.btn-small{display:inline-block;margin-top:8px;background:var(--brand);font-size:12px;padding:3px 16px;border-radius:2px}

/* team */
.team-photo{left:265px;top:1968px;width:669px;height:384px;background:linear-gradient(120deg,#f0f3f7 0,#c8d1dc 40%,#5c6f8a 75%,#273a57 100%)}
.team-card{left:284px;top:2303px;width:360px;height:126px;background:var(--brand);padding:16px 22px}
.team-card h3{font-size:34px;font-weight:400;margin-bottom:10px}
.team-card p{font-size:15px;font-style:italic;font-weight:300;line-height:21px;padding-left:6px}
.btn-outline{border:1px solid var(--white);display:flex;align-items:center;justify-content:center;font-size:14px;border-radius:2px}

/* partners */
.partner{top:2617px;width:183px;height:82px;background:var(--white);display:flex;align-items:center;justify-content:center;gap:8px;color:#555;font-size:28px;font-weight:400}
.partner i{width:26px;height:26px;background:#777;border-radius:50%}
.partner i.sq{border-radius:0}
.slider-dot{top:2734px;width:26px;height:26px;border-radius:50%;background:var(--accent);display:flex;align-items:center;justify-content:center}
.slider-dot.dim{opacity:.35}

/* news */
.news-card{top:2902px;width:326px;height:335px;background:var(--card);border-radius:3px;padding:8px}
.news-media{height:180px}
.news-body{display:flex;gap:14px;padding:26px 0 0 10px}
.news-date{text-align:center;width:42px}
.news-date b{display:block;font-size:26px;font-weight:500;color:var(--accent);line-height:26px}
.news-date span{font-size:10.5px}
.news-body h4{font-size:15px;font-weight:500;color:var(--accent);margin-bottom:6px}
.news-body p{font-size:12px;line-height:17px;font-weight:300;margin-bottom:14px}
.news-body .btn-outline{width:98px;height:26px;font-size:12px}

/* footer */
.site-footer{left:0;top:3393px;width:1200px;height:192px;background:var(--footer)}
.footer-badge{left:88px;top:3434px;width:116px;height:116px;border-radius:50%;background:var(--white);border:3px solid var(--brand);display:flex;flex-direction:column;align-items:center;justify-content:center;color:var(--brand)}
.footer-badge b{font-weight:600;font-size:24px}
.footer-badge small{font-size:7px;color:var(--navy)}
.footer-meta{left:0;width:1200px;top:3466px;text-align:center;font-size:13px;color:var(--accent);font-weight:300}
.footer-links{left:0;width:1200px;top:3494px;display:flex;justify-content:center;gap:40px;font-size:14px;padding-right:0}
.footer-links .active{text-decoration:underline;text-underline-offset:4px}
.social{left:1069px;top:3465px;width:42px;height:42px;border-radius:50%;background:var(--white)}
.footer-base{left:0;top:3585px;width:1200px;height:43px;background:var(--footer-base);text-align:center;font-size:12px;line-height:43px;font-weight:300}
</style>
</head>
<body>

<header class="site-header abs"></header>
<a class="nav-link abs active" style="left:89px">CDaaS</a>
<a class="nav-link abs" style="left:176px">Security Services</a>
<a class="nav-link abs" style="left:335px">Compliance</a>
<div class="brand-badge abs"><b>Corvane</b><small>IT · Security · Compliance</small></div>
<a class="nav-link abs" style="left:797px">Company</a>
<a class="nav-link abs" style="left:903px">Career</a>
<a class="nav-link abs" style="left:990px">Contact</a>
<svg class="flag abs" viewBox="0 0 32 21" aria-label="Deutsch"><rect width="32" height="7" fill="#111"/><rect y="7" width="32" height="7" fill="#d00"/><rect y="14" width="32" height="7" fill="#fc0"/></svg>

<h1 class="hero-title abs">Die IT-Sicherheit Ihrer IT-Infrastruktur ist unsere Mission.</h1>
<p class="hero-text abs">Unsere Cybersicherheitsdienste sind rund um den Kunden konzipiert. Wir bieten eine robuste Zusammenarbeit, um die Herausforderungen Ihrer Umgebung zu verstehen und maßgeschneiderte, sichere Lösungen zu entwickeln.</p>
<div class="hero-visual abs" role="img" aria-label="Isometric illustration of a laptop protected by a glowing security shield"></div>

<article class="service-card abs" style="left:87px">
  <svg viewBox="0 0 62 62" fill="none" stroke="#4d93e6" stroke-width="2.5"><circle cx="31" cy="31" r="20"/><path d="M31 5v6M31 51v6M5 31h6M51 31h6M13 13l4 4M45 45l4 4M49 13l-4 4M13 49l4-4"/><rect x="23" y="29" width="16" height="12" rx="2"/><path d="M26 29v-4a5 5 0 0 1 10 0v4"/></svg>
  <h3>CDaas-Cyber Defense as a Service</h3>
  <p>Our all-in-one CDaaS offer offers a convenient integration of your IT infrastructure into an active and comprehensive security solution.</p>
</article>
<article class="service-card abs" style="left:437px;padding-top:20px">
  <svg viewBox="0 0 62 62" fill="none" stroke="#4d93e6" stroke-width="2.5"><path d="M33 6l16 6v14c0 11-7 18-16 22-9-4-16-11-16-22V12z"/><path d="M26 27l5 5 9-10"/><path d="M6 50c6-6 12-6 18-2h10a3 3 0 0 1 0 6H22"/></svg>
  <h3>Security Services</h3>
  <p>Our security services provide you with comprehensive support in the planning and implementation of your holistic IT and information management.</p>
</article>
<article class="service-card abs" style="left:786px;padding-top:20px">
  <svg viewBox="0 0 62 62" fill="none" stroke="#4d93e6" stroke-width="2.5"><rect x="12" y="6" width="32" height="46" rx="2"/><path d="M18 16l3 3 5-5M30 17h9M18 28l3 3 5-5M30 29h9M18 40l3 3 5-5M30 41h4"/><circle cx="46" cy="46" r="9"/><path d="M42 46l3 3 5-6"/></svg>
  <h3>Compliance</h3>
  <p>We support you with your IT security at the highest level with an effective compliance strategy.</p>
</article>

<h2 class="section-title abs" style="top:910px">Vision &amp; Mission</h2>
<div class="tab current abs" style="top:983px">Vision</div>
<div class="tab abs" style="top:1043px">Mission</div>
<div class="tab abs" style="top:1104px">Portfolio</div>
<div class="vision-panel abs">
  <h4>Holistic IT security is our claim.</h4>
  <p>We stand for your IT security. We offer extensive services and our certified IT experts work with you to ensure that your systems are secure.</p>
  <h5>With us you have:</h5>
  <p>• Fastest response times 24x7<br>• Market<br>leading technologies<br>• Certified cyber analysts with the highest level of expertise</p>
  <p>The "Pay-As-You-Grow" model allows ongoing adjustments to the professional security services used - with one claim: your needs.</p>
</div>

<h2 class="section-title abs" style="top:1372px">Industry Sectors</h2>
<p class="section-sub abs" style="top:1420px">Sample text. Click to select the text box. Click again or double click to start editing the text.</p>
<div class="sector-tile abs" role="img" aria-label="Hand touching digital finance security icons" style="left:88px;top:1473px;background:linear-gradient(180deg,#3c5a78,#0c1a2b)">Financial Sector</div>
<div class="sector-tile sector-ops abs" style="left:438px;top:1473px">
  <h3>It Service OPS</h3>
  <ul><li>Event Management</li><li>Incident Management</li></ul>
  <span class="btn-small">Read More</span>
</div>
<div class="sector-tile abs" role="img" aria-label="Engineers at monitors in a car design studio" style="left:787px;top:1473px;background:linear-gradient(180deg,#34506e,#0b1522)">Automobil Industrie</div>
<div class="sector-tile abs" role="img" aria-label="Solar panels and wind turbines at sunset" style="left:88px;top:1692px;background:linear-gradient(180deg,#6b7f94,#a08a6a 45%,#1c2533)">Energy</div>
<div class="sector-tile abs" role="img" aria-label="Tablet with logistics network icons" style="left:438px;top:1692px;background:linear-gradient(180deg,#3f6685,#12233a)">Logistics</div>
<div class="sector-tile abs" role="img" aria-label="Scales of justice on a desk" style="left:787px;top:1692px;background:linear-gradient(100deg,#1d1f22,#6f6454 50%,#b9b1a4)">Governorate</div>

<div class="team-photo abs" role="img" aria-label="Business handshake across an office desk"></div>
<div class="team-card abs"><h3>Working at Corvane</h3><p>"We rely on trust, reliability<br>and professionalism"</p></div>
<a class="btn-outline abs" style="left:667px;top:2372px;width:234px;height:40px">Become Part of The Team</a>

<h2 class="section-title abs" style="top:2518px">Patient Resources</h2>
<p class="section-sub abs" style="top:2566px">We will find the best solution for you. We develop a wide range of services with our individual solutions.</p>
<div class="partner abs" style="left:94px"><i></i>nimbra</div>
<div class="partner abs" style="left:301px;font-size:22px"><i class="sq"></i>Solvexa</div>
<div class="partner abs" style="left:508px;font-size:22px"><i class="sq"></i>Tarnfield</div>
<div class="partner abs" style="left:715px">Quorix</div>
<div class="partner abs" style="left:922px;font-size:34px">veltro</div>
<div class="slider-dot dim abs" style="left:567px"><svg width="14" height="14" viewBox="0 0 14 14" fill="none" stroke="#0a2342" stroke-width="2"><path d="M12 7H2M6 3L2 7l4 4"/></svg></div>
<div class="slider-dot abs" style="left:604px"><svg width="14" height="14" viewBox="0 0 14 14" fill="none" stroke="#0a2342" stroke-width="2"><path d="M2 7h10M8 3l4 4-4 4"/></svg></div>

<h2 class="section-title abs" style="top:2828px">Latest News</h2>
<article class="news-card abs" style="left:87px">
  <div class="news-media" role="img" aria-label="Gavel and scales on a lawyer's desk" style="background:linear-gradient(90deg,#2c2620,#8a7a62 50%,#e3ddd2)"></div>
  <div class="news-body"><div class="news-date"><b>21</b><span>Sep, 22</span></div><div><h4>Post 4 headline</h4><p>Example small text. Lorem ipsum dolor sit amet.</p><a class="btn-outline">Read More</a></div></div>
</article>
<article class="news-card abs" style="left:437px">
  <div class="news-media" role="img" aria-label="Laptops surrounded by glowing security shields" style="background:radial-gradient(circle,#2f7fe0,#142f7a 60%,#0b1a46)"></div>
  <div class="news-body"><div class="news-date"><b>21</b><span>Sep, 22</span></div><div><h4>Post 4 headline</h4><p>Example small text. Lorem ipsum dolor sit amet.</p><a class="btn-outline">Read More</a></div></div>
</article>
<article class="news-card abs" style="left:786px">
  <div class="news-media" role="img" aria-label="Isometric server racks in a data center" style="background:radial-gradient(circle at 60% 45%,#5a9cff,#1d47b8 50%,#0d1f5e)"></div>
  <div class="news-body"><div class="news-date"><b>21</b><span>Sep, 22</span></div><div><h4>Post 4 headline</h4><p>Example small text. Lorem ipsum dolor sit amet.</p><a class="btn-outline">Read More</a></div></div>
</article>
<a class="btn-outline abs" style="left:546px;top:3273px;width:107px;height:40px">View All</a>

<footer class="site-footer abs"></footer>
<div class="footer-badge abs"><b>Corvane</b><small>IT · Security · Compliance</small></div>
<p class="footer-meta abs">© Corvane (S.à rl) • Tel.: +352 4817 20 30 - 10</p>
<nav class="footer-links abs"><a class="active">Contact</a><a>Imprint</a><a>Privacy</a><a>Legal Notice</a></nav>
<a class="social abs" aria-label="Social profile"></a>
<div class="footer-base abs">Copyright © 2022 Corvane. All Rights Reserved</div>

</body>
</html>
```